Digital Menu Board for Restaurant

I want a digital menu board for our new restaurant. I have provided the sample of what I kind of want.
This is to be on a 55 inch tv so it needs to be the correct aspect ratio of 4:5

Font styles to use
Serif
Sans Serif

Colors
f59296
f04a50
ec1f27
ffffff
fffef7
fbed22
ffc214
0592cd
e5519f

Requirements
Must have
• fun, maybe something moving? bright colors on a darker background so it's easy to read or dark font on a light background.

```html
<!DOCTYPE html>
<html lang="en">
<head>
<meta charset="utf-8">
<title>Sandy Coves Menu Board</title>
<link href="https://fonts.googleapis.com/css2?family=Lato:ital,wght@0,400;0,700;0,900;1,400;1,700&display=swap" rel="stylesheet">
<style>
  :root {
    --cream: #fffef7;
    --ink: #23285e;
    --red: #f04a50;
    --red-deep: #ec1f27;
    --salmon: #f59296;
    --sun: #fbed22;
    --sun-soft: #f8f08a;
    --gold: #ffc214;
    --sky: #0592cd;
    --berry: #e5519f;
    --lavender: #d3d0df;
    --blush: #f8cfcf;
    --pinkring: #f5c7df;
  }
  * { margin: 0; padding: 0; box-sizing: border-box; }
  html, body { width: 961px; height: 1200px; overflow: hidden; background: var(--cream); }
  .board {
    position: relative; width: 961px; height: 1200px; overflow: hidden;
    background: var(--cream); font-family: "Lato", sans-serif; color: var(--ink);
  }
  .decor { position: absolute; inset: 0; width: 961px; height: 1200px; }
  .brand {
    position: absolute; left: 48px; top: 150px; display: flex; align-items: center; gap: 14px;
  }
  .brand-dot { width: 30px; height: 30px; border-radius: 50%; background: var(--gold); }
  .brand-name { font-weight: 900; font-size: 62px; color: var(--red); letter-spacing: 0.5px; line-height: 1; }

  .combo { position: absolute; left: 585px; top: 92px; }
  .combo-title { font-weight: 900; font-size: 34px; color: var(--red-deep); line-height: 1.1; margin-bottom: 5px; }
  .combo-line { font-weight: 700; font-size: 24.5px; color: var(--ink); line-height: 34.5px; }

  .heading { position: absolute; font-weight: 900; font-size: 24px; color: var(--red); line-height: 1; letter-spacing: 0.2px; }

  .item { position: absolute; left: 49px; width: 382px; }
  .item-name { font-weight: 700; font-size: 19.5px; line-height: 22px; }
  .item-name.slanted { font-style: italic; }
  .item-name sup { font-size: 11px; }
  .item-desc { font-style: italic; font-size: 15.4px; line-height: 22px; margin-top: 1px; }
  .item-add { font-style: italic; font-weight: 700; font-size: 15.4px; line-height: 22px; }

  .list { position: absolute; list-style: none; font-size: 20px; line-height: 26.7px; color: var(--ink); }
</style>
</head>
<body>
<main class="board">
  <svg class="decor" viewBox="0 0 961 1200">
    <defs>
      <radialGradient id="glow-sky"><stop offset="0" stop-color="#0592cd" stop-opacity="0.28"/><stop offset="1" stop-color="#0592cd" stop-opacity="0"/></radialGradient>
      <radialGradient id="glow-salmon"><stop offset="0" stop-color="#f59296" stop-opacity="0.35"/><stop offset="1" stop-color="#f59296" stop-opacity="0"/></radialGradient>
      <radialGradient id="glow-gold"><stop offset="0" stop-color="#ffc214" stop-opacity="0.32"/><stop offset="1" stop-color="#ffc214" stop-opacity="0"/></radialGradient>
      <linearGradient id="wave-band" x1="0" y1="0" x2="0" y2="1"><stop offset="0" stop-color="#0592cd" stop-opacity="0.15"/><stop offset="0.5" stop-color="#0592cd" stop-opacity="0.32"/><stop offset="1" stop-color="#0592cd" stop-opacity="0.15"/></linearGradient>
    </defs>
    <circle cx="703" cy="111" r="184" fill="var(--sun)"/>
    <circle cx="572" cy="422" r="104" fill="none" stroke="var(--lavender)" stroke-width="26"/>
    <circle cx="211" cy="711" r="100" fill="none" stroke="var(--blush)" stroke-width="26"/>
    <circle cx="33" cy="600" r="42" fill="none" stroke="var(--sun-soft)" stroke-width="12"/>
    <circle cx="283" cy="441" r="13" fill="none" stroke="var(--salmon)" stroke-width="4"/>
    <circle cx="333" cy="922" r="52" fill="none" stroke="var(--pinkring)" stroke-width="14"/>
    <circle cx="211" cy="1200" r="104" fill="none" stroke="var(--lavender)" stroke-width="26"/>
    <circle cx="711" cy="978" r="222" fill="none" stroke="var(--sun-soft)" stroke-width="48"/>
    <circle cx="961" cy="1005" r="48" fill="none" stroke="var(--lavender)" stroke-width="14"/>
    <ellipse cx="842" cy="275" rx="70" ry="115" fill="url(#glow-sky)" role="img" aria-label="Blue dot grid pattern"/>
    <ellipse cx="867" cy="658" rx="60" ry="145" fill="url(#glow-salmon)" role="img" aria-label="Pink dot grid pattern"/>
    <ellipse cx="389" cy="442" rx="45" ry="80" fill="url(#glow-gold)" role="img" aria-label="Yellow dot grid pattern"/>
    <ellipse cx="483" cy="664" rx="45" ry="52" fill="url(#glow-salmon)" role="img" aria-label="Pink dot trail pattern"/>
    <ellipse cx="32" cy="964" rx="45" ry="80" fill="url(#glow-salmon)" role="img" aria-label="Pink dot grid pattern"/>
    <rect x="0" y="1139" width="961" height="40" fill="url(#wave-band)" role="img" aria-label="Blue wave pattern band"/>
  </svg>

  <div class="brand">
    <span class="brand-dot"></span>
    <span class="brand-name">Sandy Coves</span>
  </div>

  <section class="combo">
    <h2 class="combo-title">COMBO UP</h2>
    <p class="combo-line">Add 1 side and drink</p>
    <p class="combo-line">Add 1 side and shake</p>
    <p class="combo-line">Additional Sides</p>
  </section>

  <h2 class="heading" style="left:49px; top:317px;">BETWEEN BUNS</h2>

  <article class="item" style="top:346px;">
    <h3 class="item-name">1<sup>st</sup> Point Pulled Pork</h3>
    <p class="item-desc">Pulled Pork, Mack’s Sassy BBQ Sauce, Chopped Bacon, Pepperjack Cheese, and Fried Jalapeño Pepper on a Ciabatta Bun</p>
  </article>
  <article class="item" style="top:453px;">
    <h3 class="item-name">2<sup>nd</sup> Point Pulled Pork</h3>
    <p class="item-desc">Pulled Pork, Mack’s Sweet Raspberry BBQ Sauce, and Coleslaw on a Ciabatta Bun</p>
  </article>
  <article class="item" style="top:539px;">
    <h3 class="item-name">Spiniker Point Burger</h3>
    <p class="item-desc">Smokerhouse 1/2 Pound Burger, Crumbled Bacon, Mack’s Sassy BBQ Sauce, Cheese, and Onion Rings on a Toasted Brioche Bun</p>
  </article>
  <article class="item" style="top:647px;">
    <h3 class="item-name">The Rock Burger</h3>
    <p class="item-desc">Two Smokerhouse 1/2 Pound Patties, Cheese, Lettuce, Tomato, Onion, Pickles on a Toasted Brioche Bun</p>
  </article>
  <article class="item" style="top:732px;">
    <h3 class="item-name">Rainbow Cove Sandwich</h3>
    <p class="item-desc">Chicken Salad - Smoked Chicken, Celery and Onion Mixed with Our BBQ Mayo and Topped with Seasoned Tomato on a Hoagie Roll</p>
  </article>
  <article class="item" style="top:839px; width:425px;">
    <h3 class="item-name slanted">North Beach Salad</h3>
    <p class="item-desc">Pulled Pork and Black Bean on a Bed Of Romaine, Tomato and Onion with Sweet and Sour Raspberry Pineapple Sauce.</p>
  </article>
  <article class="item" style="top:926px;">
    <h3 class="item-name">West Side Salad</h3>
    <p class="item-desc">Bbq Pulled Pork, Crumbled Bacon, Candied Walnuts, Feta Cheese, Red Onion, Spinach and Lecture with Ranch Dressing or Raspberry Vinaigrette</p>
  </article>
  <article class="item" style="top:1033px;">
    <h3 class="item-name">East Side Salad</h3>
    <p class="item-desc">Spinach and Lettuce, Chopped Apples, Candied Walnuts, Onion, Feta Cheese with Mack’s Rasberry Vinaigrette</p>
    <p class="item-add">Add Chicken</p>
  </article>

  <h2 class="heading" style="left:522px; top:317px;">SIDES</h2>
  <ul class="list" style="left:522px; top:343px;">
    <li>Seasoned Fries</li><li>Onion Rings</li><li>Sweet Cornbread</li>
  </ul>
  <ul class="list" style="left:730px; top:339px;">
    <li>Sweet Coleslaw</li><li>Macaroni Salad</li><li>Side Salad</li>
  </ul>

  <h2 class="heading" style="left:522px; top:456px;">SEASHELL FINDERS (KIDS)</h2>
  <ul class="list" style="left:522px; top:482px;">
    <li>Little Cheeseburger</li><li>Pulled Pork Sandwich</li><li>Mini Corn Dogs</li><li>Chicken Salad Sandwich</li><li>Fries / Onion Rings</li>
  </ul>

  <h2 class="heading" style="left:522px; top:648px;">DRINKS</h2>
  <ul class="list" style="left:522px; top:674px;">
    <li>Fizz Cola</li><li>Diet Fizz</li><li>Red Cola</li><li>Diet Red</li><li>Peak Soda</li>
  </ul>
  <ul class="list" style="left:730px; top:674px;">
    <li>Diet Peak</li><li>Lemonade</li><li>Lime Pop</li><li>Dr Spice</li>
  </ul>

  <h2 class="heading" style="left:522px; top:839px;">SHAKE</h2>
  <ul class="list" style="left:522px; top:865px;">
    <li>Mack’s Signature Raspberry Jammin Shake</li>
    <li>Raspberry Cookie Crumble Shake</li>
    <li>Raspberry Hazelnut Cocoa Bomb Shake</li>
    <li>Raspberry Beachin’ Shake (Pina Colada)</li>
    <li>Raspberry Brownies Shake</li>
    <li>Caramel Shake</li>
    <li>Chocolate Shake</li>
  </ul>
</main>
</body>
</html>
```